LIFE CHANGING NEW WEBSITE DESIGN NEEDED FOR FULL WEBSITE- FUN/FEMININE!

I need a website designed for a personal financial advice website geared at women called DAME CLOVER HAVEN. I will be providing free financial advice around topics of making, saving, spending and sharing money. The concept is to change the way women understand money and the necessity around building various passive income streams to ensure full financial freedom. This will then carry down to advice for mothers with children and children in particular. The website should be elegant and yet witty. I don't want lots of serious photos but more relatable. I will have a photo of myself and my story as this is a blog and needs to be relatable to women and mothers. I like pinks and greys. I want to have a pink piggy bank being broken with a hammer in the front screen to break our traditional mindset around piggy bank saving/spending habits. I have created a logo that is a pink piggy head with DAME CLOVER HAVEN that needs to be incorporated so that it blends into the heading. I have also already started designing the website on Squarespace and can provide access to that. Basically it should have a format of DAME CLOVER HAVEN LOGO center in header then on left hand navigation: MAKE, SAVE, SPEND, SHARE then on right hand header navigation: MISSION, GET STARTED, CONTACT DCH I would like to have the front page when you go to the url to have the image of the piggy bank being broken then a catchy phrase then under 4 boxes with MAKE (image and description) SAVE (image and description) SPEND (image and description) SHARE (image and description) if you click on those or the title they go to pages that are dedicated to each them. Each page should have a little intro on the topic then I want lots of blog links as I will be mainly writing blogs. Each blog site should have ability to write comments as well. I need social media icons on each page too. Please let me know what you need from me to get started. I prefer having a discussion if possible to not waste anyone's time. I need the site to be easy for me to use and add blogs/urls etc as needed. I also need the site to be put into my domain that I already purchased: www.damecloverhaven.com

Target Market(s)

teenage girls, 20 something girls, 30 something girls and mothers

Coding

Coded - Design and coding required

Number of Pages Required

5+ page

Font styles to use
Sans Serif

Colors
e667a6
e34197
f59195
eea4c8
aaaaaa
cbcbcb
959595

Requirements
Must have
• TOP NAVIGATION
• MAKE SAVE SPEND SHARE LOGO/DAME CLOVER HAVEN MISSION GET STARTED CONTACT DCH
• FRONT PAGE: IMAGE OF PIGGY BANK BEING BROKEN WITH A HAMMER
• CATCH PHRASE OVER THE IMAGE
• BUTTON IN PINK- TAKE ACTION (WHICH DIRECTS TO TAKE ACTION TAB ON NAVIGATION HEADER
• 4 BOXES BELOW MAIN IMAGE WITH IMAGE/DESCRIPTIONS FOR MAKE, SAVE, SPEND, SHARE THAT EACH GO TO THE PAGES FROM THE NAVIGATION HEADER
• EACH PAGE SHOULD BE DEDICATED TO THOSE TOPICS THEN THERE IS AN INTRO ON EACH PAGE THEN THE LINKS TO DIFFERENT BLOGS AROUND EACH TOPIC FOR MAKE, SAVE, SPEND, SHARE
• EACH BLOG SHOULD HAVE COMMENTS SECTION AND SOCIAL MEDIA ICONS
• (GOOD TO USE PINKS/GREYS)
Should not have
• BE SUPER BUSY, CLUTTERED, FEEL LIKE I AM SELLING SOMETHING

```html
<!DOCTYPE html>
<html lang="en">
<head>
<meta charset="utf-8">
<title>Dame Clover Haven</title>
<link href="https://fonts.googleapis.com/css2?family=Montserrat:wght@400;500;600;700&family=Lato:wght@400;700&display=swap" rel="stylesheet">
<style>
:root{
  --pink:#e0258a;
  --pink-soft:#e667a6;
  --pink-pale:#eea4c8;
  --grey-dark:#3c3c3c;
  --grey:#959595;
  --grey-mid:#aaaaaa;
  --grey-light:#cbcbcb;
  --card-bg:#f2f2f2;
  --white:#ffffff;
  --text:#555555;
}
*{box-sizing:border-box;margin:0;padding:0}
html,body{width:1200px;height:3578px;overflow:hidden}
body{position:relative;background:var(--white);font-family:'Lato',sans-serif;color:var(--text)}
.abs{position:absolute}
.top-line{left:0;top:0;width:1200px;height:4px;background:var(--pink)}
.nav{top:75px;font-family:'Montserrat',sans-serif;font-size:11px;font-weight:500;letter-spacing:.4px;color:var(--grey-dark);display:flex;gap:27px}
.nav-left{left:171px}
.nav-right{left:754px}
.brand{left:450px;top:22px;width:300px;text-align:center}
.brand-dot{width:30px;height:30px;border:2px solid var(--pink);border-radius:50%;margin:0 auto 8px}
.brand-name{font-family:'Montserrat',sans-serif;font-size:20px;font-weight:500;color:var(--pink)}
.hero{left:0;top:118px;width:1200px;height:571px;background:linear-gradient(135deg,#4a3a30 0%,#6b5546 35%,#8a4a55 55%,#5e4c40 80%,#3e342c 100%)}
.hero-title{left:0;top:326px;width:1200px;text-align:center;font-family:'Montserrat',sans-serif;font-weight:700;font-size:43px;color:var(--white);letter-spacing:.5px}
.hero-sub{left:0;top:393px;width:1200px;text-align:center;font-family:'Montserrat',sans-serif;font-weight:500;font-size:23px;line-height:26px;color:var(--white)}
.hero-btn{left:536px;top:460px;width:128px;height:39px;border-radius:20px;background:var(--pink);color:var(--white);font-family:'Montserrat',sans-serif;font-size:13px;font-weight:500;display:flex;align-items:center;justify-content:center}
.hero-arrow{top:373px;width:33px;height:33px;border:1.5px solid var(--white);border-radius:50%}
.card{top:792px;width:203px;height:333px;background:var(--card-bg)}
.card-photo{width:203px;height:172px}
.card-title{position:absolute;left:15px;top:190px;font-family:'Montserrat',sans-serif;font-size:16px;font-weight:500;color:var(--grey-dark)}
.card-text{position:absolute;left:15px;top:217px;width:175px;font-size:10px;line-height:15px;color:var(--grey-dark)}
.card-btn{position:absolute;left:15px;top:290px;padding:0 13px;height:24px;border-radius:12px;background:var(--pink);color:var(--white);font-family:'Montserrat',sans-serif;font-size:10px;display:flex;align-items:center}
.welcome-photo{left:0;top:1247px;width:796px;height:616px;background:linear-gradient(120deg,#c9c3b8,#a89888 40%,#d8d2c8 70%,#efece6)}
.welcome-dots{left:848px;top:1247px;width:352px;height:336px;background:#f6f6f6}
.welcome-box{left:537px;top:1315px;width:534px;height:481px;background:var(--pink);color:var(--white);padding:52px 66px 0 55px}
.welcome-box h2{font-family:'Montserrat',sans-serif;font-size:27px;font-weight:500;line-height:33px}
.welcome-box .mission{margin-top:22px;font-size:11px;line-height:19.5px}
.welcome-box .mission u{text-decoration:underline}
.welcome-box .story{margin-top:20px;font-size:10.5px;line-height:19.5px;text-align:justify}
.outline-btn{display:inline-block;margin-top:20px;padding:0 13px;height:27px;line-height:25px;border:1.5px solid var(--white);border-radius:14px;font-size:11px}
.section-title{left:0;top:1944px;width:1200px;text-align:center;font-family:'Montserrat',sans-serif;font-size:26px;font-weight:500;color:var(--grey-dark)}
.post{left:167px;width:900px;height:215px}
.post-frame-v{position:absolute;left:0;top:15px;width:4px;height:200px;background:var(--pink)}
.post-frame-h{position:absolute;left:0;top:211px;width:220px;height:4px;background:var(--pink)}
.post-photo{position:absolute;left:5px;top:0;width:341px;height:207px}
.post-title{position:absolute;left:369px;top:10px;width:420px;font-family:'Montserrat',sans-serif;font-size:17.5px;font-weight:600;line-height:22px;color:var(--pink)}
.post-text{position:absolute;left:369px;top:67px;width:420px;font-size:10.5px;line-height:20px;color:var(--grey-dark)}
.post-meta{position:absolute;left:369px;top:171px;font-family:'Montserrat',sans-serif;font-size:11px;font-weight:500;color:var(--grey-dark);display:flex;gap:20px;align-items:center}
.post-meta span{display:flex;align-items:center;gap:5px}
.post-meta u{text-decoration:underline}
.share{position:absolute;left:834px;top:34px;display:flex;flex-direction:column;gap:8px}
.share i{display:block;width:23px;height:23px;border:1.5px solid var(--grey);border-radius:50%}
.share i.first{border-color:var(--pink)}
.pager{top:3063px;left:529px;display:flex;gap:6px}
.pager span{width:31px;height:31px;display:flex;align-items:center;justify-content:center;font-family:'Montserrat',sans-serif;font-size:11px;background:var(--grey-light);color:var(--grey-dark)}
.pager span.on{background:var(--pink-pale)}
.footer-left{left:0;top:3164px;width:474px;height:414px;background:var(--pink)}
.footer-right{left:474px;top:3164px;width:726px;height:414px;background:linear-gradient(135deg,#8e8e8e,#a5a5a5 50%,#9a9a9a)}
.f-head{font-family:'Montserrat',sans-serif;font-size:16px;font-weight:500;color:var(--white)}
.f-text{font-size:11px;line-height:22px;color:var(--white)}
.field{left:172px;width:250px;height:34px;border:1.5px solid var(--white);border-radius:17px;padding-left:17px;font-size:10px;color:var(--white);display:flex;align-items:center}
.signup{left:172px;top:3411px;width:250px;height:34px;border-radius:17px;background:#8a8a8a;border:1.5px solid var(--white);color:var(--white);font-family:'Montserrat',sans-serif;font-size:13px;font-weight:500;display:flex;align-items:center;justify-content:center}
.f-icon-head{display:flex;align-items:center;gap:9px}
.bottom-bar{left:0;top:3517px;width:1200px;height:1px;background:rgba(255,255,255,.35)}
.social{top:3538px;left:172px;display:flex;gap:30px}
.social i{display:block;width:20px;height:20px;border:2px solid var(--white);border-radius:50%}
.copy{left:768px;top:3542px;font-size:11px;color:var(--white)}
</style>
</head>
<body>
<div class="abs top-line"></div>

<nav class="abs nav nav-left"><span>MAKE</span><span>SAVE</span><span>SPEND</span><span>SHARE</span></nav>
<div class="abs brand"><div class="brand-dot"></div><div class="brand-name">Dame Clover Haven</div></div>
<nav class="abs nav nav-right"><span>MISSION</span><span>GET STARTED</span><span>CONTACT DCH</span></nav>

<section>
  <div class="abs hero" role="img" aria-label="Pink piggy bank being broken with a hammer among scattered coins and notes"></div>
  <div class="abs hero-arrow" style="left:35px"><svg width="30" height="30" viewBox="0 0 30 30"><path d="M17 10l-5 5 5 5" fill="none" stroke="#fff" stroke-width="1.5"/></svg></div>
  <div class="abs hero-arrow" style="left:1130px"><svg width="30" height="30" viewBox="0 0 30 30"><path d="M13 10l5 5-5 5" fill="none" stroke="#fff" stroke-width="1.5"/></svg></div>
  <h1 class="abs hero-title">DAME CLOVER HAVEN</h1>
  <p class="abs hero-sub">Sed ut perspiciatis unde omnis iste natusvolup<br>tatem accusa ntium doloremque daa rem.</p>
  <div class="abs hero-btn">TAKE ACTION</div>
</section>

<section>
  <article class="abs card" style="left:172px">
    <div class="card-photo" role="img" aria-label="Hands using a calculator beside a pink piggy bank" style="background:linear-gradient(135deg,#d9d4cf,#e8c9c9)"></div>
    <h3 class="card-title">MAKE</h3>
    <p class="card-text">Sed ut perspiciatis unde omnis iste natus error sit voluptatem accusa ntium doloremque laudantitum rem aperiam, eaque isa</p>
    <span class="card-btn">Read More</span>
  </article>
  <article class="abs card" style="left:390px">
    <div class="card-photo" role="img" aria-label="Smiling couple dropping a coin into a piggy bank" style="background:linear-gradient(135deg,#7a4a36,#c98a6e)"></div>
    <h3 class="card-title">SAVE</h3>
    <p class="card-text">Sed ut perspiciatis unde omnis iste natus error sit voluptatem accusa ntium doloremque laudantitum rem aperiam, eaque isa</p>
    <span class="card-btn">Read More</span>
  </article>
  <article class="abs card" style="left:607px">
    <div class="card-photo" role="img" aria-label="Hands counting banknotes over a laptop" style="background:linear-gradient(135deg,#5c6a80,#b7a59e)"></div>
    <h3 class="card-title">SPEND</h3>
    <p class="card-text">Sed ut perspiciatis unde omnis iste natus error sit voluptatem accusa ntium doloremque laudantitum rem aperiam, eaque isa</p>
    <span class="card-btn">Read More</span>
  </article>
  <article class="abs card" style="left:824px">
    <div class="card-photo" role="img" aria-label="Woman holding a phone with floating coin symbols" style="background:linear-gradient(135deg,#8a8f9c,#c9a58e)"></div>
    <h3 class="card-title">SHARE</h3>
    <p class="card-text">Sed ut perspiciatis unde omnis iste natus error sit voluptatem accusa ntium doloremque laudantitum rem aperiam, eaque isa</p>
    <span class="card-btn">Read More</span>
  </article>
</section>

<section>
  <div class="abs welcome-dots" role="img" aria-label="Light dotted background pattern"></div>
  <div class="abs welcome-photo" role="img" aria-label="Happy couple meeting a financial advisor at a desk"></div>
  <div class="abs welcome-box">
    <h2>Welcome to<br>Dame Clover Haven (DCH)!</h2>
    <p class="mission">My mission is simple- I want to challenge you to <u>rethink the way you think about growing, spending and saving money. By redesigning your life around your finances I want you to run your life as if you are the CEO of your own business, and the business is maximising the value and profitability of your life.</u></p>
    <p class="story">It is shocking that in today's world of information we are we still live in a society where most educated people leave school without even a basic understanding of money and how to run their lives outside of a just obtaining a job. Instead, we are taught to work hard in school, find a good job, get married, have children, save up for big expenses (like homes, school tuition..) then retire. By completely lacking personal finance education in schools and few resources to help, it is little wonder that life often feels like one big rat race of no end.</p>
    <span class="outline-btn">Read More</span>
  </div>
</section>

<h2 class="abs section-title">Latest Blog Posts</h2>

<section>
  <article class="abs post" style="top:2031px">
    <div class="post-frame-v"></div><div class="post-frame-h"></div>
    <div class="post-photo" role="img" aria-label="Advisor with a laptop talking to a couple at a table" style="background:linear-gradient(135deg,#cfd6cf,#8c8f8a 60%,#e6e3dc)"></div>
    <h3 class="post-title">Sed ut perspiciatis unde omnis iste natulup tatem accusantium doloremqueaudue</h3>
    <p class="post-text">Sed ut perspiciatis unde omnis iste natus error sit voluptatem accusantium dolorloe mque laudantium, totam rem aperiam, eaque ipsa quae ab illo inventore veritatis et quasi architecto beatae vitae dicta sunt explicabo. Nemo enim ipsam voluptatemlo quia voluptas sit aspernatur aut odit aut fugit, sed quia consequuntu.</p>
    <div class="post-meta"><span><svg width="11" height="11" viewBox="0 0 11 11"><rect x=".5" y="1.5" width="10" height="9" fill="none" stroke="#3c3c3c"/><rect x=".5" y="1.5" width="10" height="3" fill="#3c3c3c"/></svg>June 18 2019</span><span><svg width="12" height="10" viewBox="0 0 12 10"><path d="M6 0C2.7 0 0 1.9 0 4.3c0 1.2.7 2.3 1.8 3L1 10l3-1.9c.6.2 1.3.2 2 .2 3.3 0 6-1.9 6-4.2S9.3 0 6 0z" fill="#3c3c3c"/></svg><u>Write a Comment</u></span></div>
    <div class="share"><i class="first"></i><i></i><i></i><i></i></div>
  </article>
  <article class="abs post" style="top:2283px">
    <div class="post-frame-v"></div><div class="post-frame-h"></div>
    <div class="post-photo" role="img" aria-label="Pink piggy bank wearing glasses beside a calculator" style="background:radial-gradient(circle at 60% 40%,#e24c97,#3a3a3a 60%,#1c1c1c)"></div>
    <h3 class="post-title">Sed ut perspiciatis unde omnis iste natulup tatem accusantium doloremqueaudue</h3>
    <p class="post-text">Sed ut perspiciatis unde omnis iste natus error sit voluptatem accusantium dolorloe mque laudantium, totam rem aperiam, eaque ipsa quae ab illo inventore veritatis et quasi architecto beatae vitae dicta sunt explicabo. Nemo enim ipsam voluptatemlo quia voluptas sit aspernatur aut odit aut fugit, sed quia consequuntu.</p>
    <div class="post-meta"><span><svg width="11" height="11" viewBox="0 0 11 11"><rect x=".5" y="1.5" width="10" height="9" fill="none" stroke="#3c3c3c"/><rect x=".5" y="1.5" width="10" height="3" fill="#3c3c3c"/></svg>June 18 2019</span><span><svg width="12" height="10" viewBox="0 0 12 10"><path d="M6 0C2.7 0 0 1.9 0 4.3c0 1.2.7 2.3 1.8 3L1 10l3-1.9c.6.2 1.3.2 2 .2 3.3 0 6-1.9 6-4.2S9.3 0 6 0z" fill="#3c3c3c"/></svg><u>Write a Comment</u></span></div>
    <div class="share"><i class="first"></i><i></i><i></i><i></i></div>
  </article>
  <article class="abs post" style="top:2536px">
    <div class="post-frame-v"></div><div class="post-frame-h"></div>
    <div class="post-photo" role="img" aria-label="Couple shaking hands with an advisor in a bright room" style="background:linear-gradient(135deg,#b99a7d,#6c7d96 55%,#d8cfc4)"></div>
    <h3 class="post-title">Sed ut perspiciatis unde omnis iste natulup tatem accusantium doloremqueaudue</h3>
    <p class="post-text">Sed ut perspiciatis unde omnis iste natus error sit voluptatem accusantium dolorloe mque laudantium, totam rem aperiam, eaque ipsa quae ab illo inventore veritatis et quasi architecto beatae vitae dicta sunt explicabo. Nemo enim ipsam voluptatemlo quia voluptas sit aspernatur aut odit aut fugit, sed quia consequuntu.</p>
    <div class="post-meta"><span><svg width="11" height="11" viewBox="0 0 11 11"><rect x=".5" y="1.5" width="10" height="9" fill="none" stroke="#3c3c3c"/><rect x=".5" y="1.5" width="10" height="3" fill="#3c3c3c"/></svg>June 18 2019</span><span><svg width="12" height="10" viewBox="0 0 12 10"><path d="M6 0C2.7 0 0 1.9 0 4.3c0 1.2.7 2.3 1.8 3L1 10l3-1.9c.6.2 1.3.2 2 .2 3.3 0 6-1.9 6-4.2S9.3 0 6 0z" fill="#3c3c3c"/></svg><u>Write a Comment</u></span></div>
    <div class="share"><i class="first"></i><i></i><i></i><i></i></div>
  </article>
  <article class="abs post" style="top:2788px">
    <div class="post-frame-v"></div><div class="post-frame-h"></div>
    <div class="post-photo" role="img" aria-label="Family with two children putting coins into a piggy bank" style="background:linear-gradient(135deg,#e9e6e1,#d6a68a 50%,#8aa0b5)"></div>
    <h3 class="post-title">Sed ut perspiciatis unde omnis iste natulup tatem accusantium doloremqueaudue</h3>
    <p class="post-text">Sed ut perspiciatis unde omnis iste natus error sit voluptatem accusantium dolorloe mque laudantium, totam rem aperiam, eaque ipsa quae ab illo inventore veritatis et quasi architecto beatae vitae dicta sunt explicabo. Nemo enim ipsam voluptatemlo quia voluptas sit aspernatur aut odit aut fugit, sed quia consequuntu.</p>
    <div class="post-meta"><span><svg width="11" height="11" viewBox="0 0 11 11"><rect x=".5" y="1.5" width="10" height="9" fill="none" stroke="#3c3c3c"/><rect x=".5" y="1.5" width="10" height="3" fill="#3c3c3c"/></svg>June 18 2019</span><span><svg width="12" height="10" viewBox="0 0 12 10"><path d="M6 0C2.7 0 0 1.9 0 4.3c0 1.2.7 2.3 1.8 3L1 10l3-1.9c.6.2 1.3.2 2 .2 3.3 0 6-1.9 6-4.2S9.3 0 6 0z" fill="#3c3c3c"/></svg><u>Write a Comment</u></span></div>
    <div class="share"><i class="first"></i><i></i><i></i><i></i></div>
  </article>
</section>

<nav class="abs pager"><span class="on">1</span><span>2</span><span>3</span><span>4</span></nav>

<footer>
  <div class="abs footer-left"></div>
  <div class="abs footer-right" role="img" aria-label="Faded grey photo of a piggy bank"></div>

  <h4 class="abs f-head" style="left:172px;top:3215px">Sign Up Newsletter</h4>
  <p class="abs f-text" style="left:172px;top:3250px;width:270px;line-height:20px">Sed ut perspiciatis unde omnis iste natus erlouror sit voluptatem accusantium dolorloe mque laudan tium, totam rem aperiam, eaque ipsa quae ab.</p>
  <div class="abs field" style="top:3322px">Name:</div>
  <div class="abs field" style="top:3367px">Email:</div>
  <div class="abs signup">SIGN UP</div>

  <h4 class="abs f-head f-icon-head" style="left:524px;top:3213px"><svg width="16" height="20" viewBox="0 0 16 20"><path d="M8 1C4.1 1 1 4 1 7.8 1 12.8 8 19 8 19s7-6.2 7-11.2C15 4 11.9 1 8 1z" fill="none" stroke="#fff" stroke-width="1.3"/><circle cx="8" cy="8" r="2.5" fill="none" stroke="#fff" stroke-width="1.3"/></svg>Address</h4>
  <p class="abs f-text" style="left:524px;top:3243px">DAME CLOVER HAVEN<br>Lorem ipsmdumodr 1211,<br>3605 KZ, loremusilslk<br>Dummy Address</p>
  <h4 class="abs f-head f-icon-head" style="left:524px;top:3355px"><svg width="20" height="14" viewBox="0 0 20 14"><rect x=".7" y=".7" width="18.6" height="12.6" fill="none" stroke="#fff" stroke-width="1.3"/><path d="M1 1l9 7 9-7" fill="none" stroke="#fff" stroke-width="1.3"/></svg>Email</h4>
  <p class="abs f-text" style="left:524px;top:3382px">hello@cloverhaven-mail.com</p>
  <h4 class="abs f-head f-icon-head" style="left:524px;top:3424px"><svg width="18" height="18" viewBox="0 0 18 18"><path d="M4 1l3 4-2 2c1 2.5 3.5 5 6 6l2-2 4 3-2 3C8 16 2 10 1 3z" fill="none" stroke="#fff" stroke-width="1.2"/></svg>Phone</h4>
  <p class="abs f-text" style="left:524px;top:3453px">030-5550142</p>

  <h4 class="abs f-head" style="left:740px;top:3215px">Links</h4>
  <p class="abs f-text" style="left:740px;top:3243px">Lorem ipsum piscin<br>Do eiusmodtsum dolor<br>Consectetur adipcin</p>
  <h4 class="abs f-head" style="left:740px;top:3335px">Information</h4>
  <p class="abs f-text" style="left:740px;top:3363px">About Us<br>Imprint<br>Contact<br>News</p>

  <h4 class="abs f-head" style="left:928px;top:3215px">About</h4>
  <p class="abs f-text" style="left:928px;top:3243px">Lorem ipsudolor<br>Consecteturiscin<br>Do eiusmodt<br>Lorem ipsumdolor<br>Consectetur scin<br>Do eiusmodt<br>Lorem ipsum dolor<br>Consecteturipiscin<br>Do eiusmodt</p>

  <div class="abs bottom-bar"></div>
  <div class="abs social"><i></i><i></i><i></i><i></i></div>
  <p class="abs copy">© 2019 DAME CLOVER HAVEN. All rights reserved.</p>
</footer>
</body>
</html>
```